Flyer for family counseling

For my family counseling I'm looking for a design for flyers. Important is not only the appearance of the flyer, but also the content design. All important contents can be found on my website: www.brigitte-volkanter.at The following items should NOT appear on the flyer: - constellation work - bereavement and palliative work My logo should definitely be on the flyer. Source files are available.

Target Market(s)

Families, individuals, children, couples in need of psychological support.

Colors

Designer to choose colors to be used in the design.

Requirements
Must have
• My logo - source files available Website and contact data Recognition value from website to flyer and vice versa
Should not have
• Mention of the constellation work and mourning and palliative work not desired.

```html
<!DOCTYPE html>
<html lang="de">
<head>
<meta charset="utf-8">
<title>Familienberatung – Flyer</title>
<link rel="stylesheet" href="https://fonts.googleapis.com/css2?family=Cinzel:wght@500&family=Lato:ital,wght@0,400;0,700;1,400&family=Roboto:wght@500;700&display=swap">
<style>
:root{
  --blue:#1a5bb0;
  --blue-dark:#1a4fa0;
  --teal:#1ba89c;
  --teal-light:#2bb3a3;
  --ink:#222;
  --grey-line:#b9bcc2;
  --footer:#474747;
  --bg:#e9eaec;
}
*{margin:0;padding:0;box-sizing:border-box}
html,body{width:1200px;height:1200px;overflow:hidden;background:var(--bg)}
.flyer{position:absolute;left:141px;top:5px;width:918px;height:1190px;background:#fff;font-family:"Lato",sans-serif;color:var(--ink);overflow:hidden;box-shadow:0 2px 8px rgba(0,0,0,.15)}
.abs{position:absolute}
.brand{left:110px;top:92px;display:flex;align-items:center;gap:10px;font-family:"Lato",sans-serif;font-weight:700;font-size:19px;letter-spacing:2px;color:var(--blue-dark)}
.brand .dot{width:22px;height:22px;border-radius:50%;background:var(--teal)}
.site-url{left:500px;top:112px;font-family:"Cinzel",serif;font-weight:500;font-size:22px;letter-spacing:.5px;color:var(--blue-dark)}
.stripe{top:163px;left:0;width:918px;height:8px}
.photo-family{left:0;top:171px;width:918px;height:352px;background:linear-gradient(100deg,#d9c7a8 0%,#efe4cc 35%,#b9a985 55%,#e9d9bd 80%,#d8c3a4 100%)}
.headline-band{left:0;top:522px;width:918px;height:78px;background:var(--blue)}
.headline{left:42px;top:534px;width:460px;font-family:"Roboto",sans-serif;font-weight:700;font-size:20px;line-height:25px;color:#fff}
.teal-panel{left:447px;top:600px;width:425px;height:535px;background:var(--teal);border-radius:0 0 14px 14px}
.portrait{left:498px;top:468px;width:320px;height:204px;border:3px solid var(--blue);border-radius:0 40px 0 40px;background:linear-gradient(135deg,#f3f1ec 0%,#e8e2d6 55%,#9fb46e 100%)}
.costs-box{left:40px;top:624px;width:392px;height:505px;border:1.5px solid var(--grey-line);border-radius:10px}
.costs-title{left:50px;top:606px;padding:0 4px;background:#fff;font-size:27px;color:var(--blue);font-weight:400}
.intro{left:50px;top:650px;width:360px;font-size:14.2px;line-height:18px;text-align:justify}
.price-row{left:50px;display:flex;align-items:baseline;gap:6px;font-size:14px}
.price-row .ico{width:13px;height:13px;align-self:center;margin-right:7px}
.price-row .amt,.law{color:var(--blue);font-size:20px;font-weight:700;font-family:"Roboto",sans-serif;font-weight:500}
.law-line{left:75px;top:1022px}
.panel-h{color:#fff;font-size:20px;font-weight:700}
.about-list{left:476px;top:715px;width:380px;list-style:none;color:#fff;font-size:14.5px;line-height:19px}
.about-list li{position:relative;padding-left:20px;margin-bottom:2px}
.about-list li::before{content:"";position:absolute;left:0;top:5px;width:10px;height:10px;border:1.5px solid #dff3f0;border-radius:50%}
.quote{left:480px;width:357px;border:1.5px solid #fff;padding:18px 14px 8px;color:#fff}
.quote p{font-style:italic;font-size:13.6px;line-height:18px;text-align:justify}
.quote .who{text-align:right;font-size:14px;margin-top:5px}
.quote .qmark{position:absolute;font-family:Georgia,serif;font-weight:700;font-size:24px;line-height:1;background:var(--teal);padding:0 3px}
.quote .open{left:8px;top:-10px}
.quote .close{right:8px;bottom:-14px}
.footer{left:0;top:1139px;width:918px;height:51px;background:var(--footer);display:flex;align-items:center;justify-content:center;gap:26px;color:#fff;font-size:14.5px}
.footer span{display:flex;align-items:center;gap:8px}
</style>
</head>
<body>
<main class="flyer">
  <div class="abs brand"><span class="dot"></span>BRIGITTE VOLKANTER</div>
  <div class="abs site-url">WWW.BRIGITTE-VOLKANTER.AT</div>
  <svg class="abs stripe" viewBox="0 0 918 8" aria-hidden="true">
    <polygon points="426,0 540,0 534,8 420,8" fill="var(--teal)"/>
    <polygon points="544,0 918,0 918,8 538,8" fill="var(--blue)"/>
  </svg>

  <div class="abs photo-family" role="img" aria-label="Foto: Beraterin im Gespräch mit einer Familie mit zwei Kindern"></div>
  <div class="abs headline-band"></div>
  <p class="abs headline">Brigitte Volkanter zeichnet sich durch Wärme, Souveränität, Ruhe und Sorgfältigkeit aus</p>

  <div class="abs teal-panel"></div>
  <div class="abs portrait" role="img" aria-label="Porträtfoto der Beraterin mit rotem Schal"></div>

  <div class="abs costs-box"></div>
  <h2 class="abs costs-title">Kosten</h2>
  <p class="abs intro">Ich begleite Sie auf Ihrem Weg: Es ist nie zu früh und selten zu spät, um Veränderungen zu setzen, die sich positiv auf Ihr Leben auswirken.</p>

  <svg width="0" height="0" style="position:absolute"><symbol id="ico" viewBox="0 0 14 14"><circle cx="7" cy="7" r="5.5" fill="none" stroke="var(--blue)" stroke-width="1.4"/><circle cx="7" cy="7" r="2.5" fill="none" stroke="var(--teal)" stroke-width="1.2"/></symbol></svg>

  <div class="abs price-row" style="top:725px"><svg class="ico"><use href="#ico"/></svg>Einzelberatung pro Stunde <span class="amt">&nbsp;€ 70,-</span></div>
  <div class="abs price-row" style="top:761px"><svg class="ico"><use href="#ico"/></svg>Paarberatung pro 1 ½ Stunden <span class="amt">&nbsp;€ 100,-</span></div>
  <div class="abs price-row" style="top:797px"><svg class="ico"><use href="#ico"/></svg>Erziehungsberatung pro Stunde <span class="amt">&nbsp;€ 70,-</span></div>
  <div class="abs price-row" style="top:833px"><svg class="ico"><use href="#ico"/></svg>Familienberatung pro 1 ½ Stunden <span class="amt">&nbsp;€ 100,-</span></div>

  <div class="abs price-row" style="top:887px"><svg class="ico"><use href="#ico"/></svg>Elternberatung nach <span class="law">§ 95 Abs. 1a AußStrG</span></div>
  <div class="abs price-row" style="top:917px"><svg class="ico"><use href="#ico"/></svg>für Paare pro Person <span class="amt">€ 30,-</span></div>
  <div class="abs price-row" style="top:947px"><svg class="ico"><use href="#ico"/></svg>oder Einzelberatung <span class="amt">€ 60,-</span></div>

  <div class="abs price-row" style="top:999px"><svg class="ico"><use href="#ico"/></svg>Familien-, Eltern- oder Erziehungsberatung nach</div>
  <div class="abs law-line law">§ 107 Abs. 3 Z 1 AußStrGt</div>
  <div class="abs price-row" style="top:1055px"><svg class="ico"><use href="#ico"/></svg>für Paare pro Person <span class="amt">€ 45,-</span></div>
  <div class="abs price-row" style="top:1085px"><svg class="ico"><use href="#ico"/></svg>oder Einzelberatung <span class="amt">€ 80,-</span></div>

  <h3 class="abs panel-h" style="left:478px;top:684px">Über mich</h3>
  <ul class="abs about-list">
    <li>Menschen in ihrer Entwicklung begleiten…</li>
    <li>Aufmerksamkeit, Ruhe und Gelassenheit…</li>
    <li>Klare Strukturen und ein richtig verstandener Zugang zu Disziplin…</li>
  </ul>

  <h3 class="abs panel-h" style="left:478px;top:804px">Voices of clients</h3>
  <blockquote class="abs quote" style="top:845px;height:143px">
    <span class="qmark open">“</span>
    <p>Brigitte Volkanter zeichnet sich durch Wärme, Souveränität, Ruhe und Sorgfältigkeit aus. Sicher und liebevoll begleitet sie durch den Prozess. Sie ist neutral, aber interessiert. Man fühlt sich gut aufgehoben, auch wenn es "ans Eingemachte" geht.</p>
    <div class="who">Frau R. Klientin</div>
    <span class="qmark close">”</span>
  </blockquote>
  <blockquote class="abs quote" style="top:1011px;height:105px">
    <span class="qmark open">“</span>
    <p>Mein Weg war voller Steine und Holz. Ich nahm den Besen in die Hand und kehrte. Frau Volkanter begleitete mich dabei.</p>
    <div class="who">Frau H. Klientin</div>
    <span class="qmark close">”</span>
  </blockquote>

  <footer class="abs footer">
    <span><svg width="16" height="16" viewBox="0 0 24 24"><path d="M6.6 10.8a15 15 0 0 0 6.6 6.6l2.2-2.2a1 1 0 0 1 1-.25 11.4 11.4 0 0 0 3.6.57 1 1 0 0 1 1 1V20a1 1 0 0 1-1 1A17 17 0 0 1 3 4a1 1 0 0 1 1-1h3.5a1 1 0 0 1 1 1c0 1.25.2 2.45.57 3.57a1 1 0 0 1-.25 1z" fill="var(--teal-light)"/></svg>43 660 418 27 95</span>
    <span><svg width="12" height="16" viewBox="0 0 12 16"><path d="M6 0a6 6 0 0 0-6 6c0 4.5 6 10 6 10s6-5.5 6-10a6 6 0 0 0-6-6zm0 8.2A2.2 2.2 0 1 1 6 3.8a2.2 2.2 0 0 1 0 4.4z" fill="var(--teal-light)"/></svg>Lindengasse 14/3/2, 1220 Wien</span>
    <span><svg width="18" height="13" viewBox="0 0 18 13"><rect x="0.5" y="0.5" width="17" height="12" fill="none" stroke="var(--teal-light)"/><path d="M1 1l8 6 8-6" fill="none" stroke="var(--teal-light)"/></svg>familienberatung@brigitte-volkanter.at</span>
  </footer>
</main>
</body>
</html>
```